Private label champagne

Hello,

I need to create a label for a bottle of champagne. I am thinking a 360 degree label which wraps the whole bottle (sleeve). I need the label to be shown flat (front and back) such as in the file entitled "example".
I would also need a render of what it would look like on a bottle of champagne with a dark/clubby backdrop.
The project is for KO9RANE nightclub in Miami and we would like the logo to be gold as well as the cap of the bottle.

For the back label there needs to be the following language as shown in the file entitled "back label"

```html
<!DOCTYPE html>
<html lang="en">
<head>
<meta charset="utf-8">
<title>KO9RANE Champagne Label</title>
<link href="https://fonts.googleapis.com/css2?family=Barlow+Condensed:wght@400;500&family=Lato:ital,wght@1,300&display=swap" rel="stylesheet">
<style>
  :root {
    --backdrop: #38383b;
    --clear-label: #444446;
    --white-label: #ffffff;
    --gold: #c9a862;
    --ink: #2a2a2c;
    --note: #b9b9bb;
    --rule: #8e8e90;
  }
  * { margin: 0; padding: 0; box-sizing: border-box; }
  html, body { width: 1200px; height: 900px; overflow: hidden; background: var(--backdrop); }
  .canvas { position: relative; width: 1200px; height: 900px; font-family: "Barlow Condensed", sans-serif; color: var(--ink); }
  .label-flat { position: absolute; left: 261px; top: 244px; width: 678px; height: 490px; }
  .label-clear { position: absolute; left: 0; top: 0; width: 678px; height: 387px; background: var(--clear-label); }
  .brand-name {
    position: absolute; left: 0; top: 168px; width: 678px;
    text-align: center;
    font-family: "Barlow Condensed", sans-serif;
    font-weight: 500; font-size: 44px; letter-spacing: 0.24em;
    line-height: 1; color: var(--gold);
  }
  .label-solid { position: absolute; left: 0; top: 387px; width: 678px; height: 103px; background: var(--white-label); }
  .col { position: absolute; top: 18px; text-align: center; text-transform: uppercase; }
  .col-importer { left: 20px; width: 162px; font-size: 7.5px; letter-spacing: 0.08em; line-height: 1.25; }
  .col-importer p { margin-bottom: 9px; }
  .col-importer .origin { margin-top: 9px; }
  .col-product { left: 220px; width: 156px; }
  .col-product .type { font-size: 17px; font-weight: 500; letter-spacing: 0.32em; margin-top: -2px; }
  .col-product .varietal { font-size: 12px; letter-spacing: 0.2em; margin-top: 10px; }
  .col-product .volume { font-size: 11px; letter-spacing: 0.14em; margin-top: 18px; }
  .col-legal { left: 426px; width: 212px; font-size: 6.8px; letter-spacing: 0.03em; line-height: 1.45; text-align: justify; text-align-last: center; }
  .col-legal strong { font-weight: 500; }
  .col-legal .sulfites { margin-top: 12px; font-size: 8px; letter-spacing: 0.08em; text-align: center; }
  .callout { position: absolute; font-family: "Lato", sans-serif; font-style: italic; font-weight: 300; font-size: 14px; color: var(--note); }
  .callout-lines { position: absolute; left: 0; top: 0; }
</style>
</head>
<body>
<div class="canvas">
  <svg class="callout-lines" width="1200" height="900" viewBox="0 0 1200 900">
    <g fill="none" stroke="#8e8e90" stroke-width="1">
      <polyline points="640,266 640,192 700,192"/>
      <polyline points="640,722 640,775 700,775"/>
    </g>
    <g fill="#8e8e90">
      <polygon points="704,192 699,189.5 699,194.5"/>
      <polygon points="704,775 699,772.5 699,777.5"/>
    </g>
  </svg>
  <span class="callout" style="left:711px; top:181px;">Transparent Label</span>
  <span class="callout" style="left:711px; top:764px;">Solid White Label</span>

  <div class="label-flat">
    <div class="label-clear">
      <div class="brand-name">KO9RANE</div>
    </div>
    <div class="label-solid">
      <div class="col col-importer">
        <p>Imported by Night Pour Imports LLC.<br>Coral Bay, FL, 33100</p>
        <p>Produced and bottled by<br>Champagne Marivaux P. et Fils<br>Verzelay-sur-Marne, 51400,</p>
        <p class="origin">Product of France</p>
      </div>
      <div class="col col-product">
        <div class="type">Champagne</div>
        <div class="varietal">100% Pinot Noir</div>
        <div class="volume">750ml Alc. 13% by Vol</div>
      </div>
      <div class="col col-legal">
        <p><strong>Government Warning:</strong> (1) According to the Surgeon General, women should not drink alcoholic beverages during pregnancy because of the risk of birth defects. (2) Consumption of alcoholic beverages impairs your ability to drive a car or operate machinery and may cause health problems</p>
        <p class="sulfites">Contains Sulfites</p>
      </div>
    </div>
  </div>
</div>
</body>
</html>
```